Hearth Lantern Promise

We need web design for an anti-gun violence campaign that will urge people to ring bells instead of shooting guns to bring in the New Year and whenever someone is killed by gun violence.
This campaign will raise funds for social agencies that help communities with social issues to help especially youth with no place to turn, play or dream. Also will fund New Gun Laws policies. Should be global in aspect but appealing to United States first.
Find poem by Sir Edwin Marchbank "Sail Past, Quiet Moon" as our theme on google.
This is a start up and nothing else to give. But need something eye catching for appeal of campaign.

Target Market(s)

Universal , more male oriented.

Industry/Entity Type

Gun

Number of Pages Required

1 page

Other font styles liked:
• Designers Can Choose

Requirements
Must have
• Strong imagery and vivid colors and bell of course.
Nice to have
• A stand out design beyond words that hit home. See attached file for website ideas

```html
<!DOCTYPE html>
<html lang="en">
<head>
<meta charset="utf-8">
<title>Hearth Lantern Promise</title>
<link href="https://fonts.googleapis.com/css2?family=Open+Sans:ital,wght@0,400;0,600;1,400&family=Titillium+Web:wght@400;600&display=swap" rel="stylesheet">
<style>
:root{
  --red:#ee1c1c;
  --red-deep:#e02020;
  --ink:#1a1a1a;
  --text:#555;
  --nav-bg:#f4f4f4;
  --line:#dcdcdc;
  --grey-panel:#8a8a8a;
  --footer:#393939;
  --footer-base:#232323;
  --footer-text:#e6e6e6;
  --white:#fff;
}
*{margin:0;padding:0;box-sizing:border-box}
html,body{width:1200px;height:2244px;overflow:hidden;background:var(--white)}
body{position:relative;font-family:"Open Sans",sans-serif;color:var(--text)}
.abs{position:absolute}
.top-rule{left:0;top:0;width:1200px;height:8px;background:var(--red)}
.brand{left:99px;top:21px;display:flex;align-items:center;gap:14px}
.brand-mark{width:78px;height:78px;background:var(--red)}
.brand-name{font-family:"Titillium Web",sans-serif;font-weight:600;font-size:31px;color:var(--ink)}
.main-nav{left:0;top:108px;width:1200px;height:58px;background:var(--nav-bg);border-top:1px solid var(--line);border-bottom:1px solid var(--line)}
.main-nav a{position:absolute;top:18px;font-family:"Titillium Web",sans-serif;font-size:15px;color:#222;text-decoration:none}
.hero{left:0;top:166px;width:1200px;height:494px;background:#000;overflow:hidden}
.hero-photo{position:absolute;left:740px;top:0;width:390px;height:494px;background:linear-gradient(180deg,#1b1b1b 0%,#2a2a2a 45%,#8a6446 70%,#e2a26b 88%,#f3c792 100%)}
.hero-quote{position:absolute;left:99px;top:160px;font-family:"Titillium Web",sans-serif;font-weight:600;font-size:24px;line-height:48px;color:var(--white)}
.hero-arrow{position:absolute;top:387px;width:30px;height:30px}
.hero-dots{position:absolute;left:580px;top:631px;display:flex;gap:8px}
.hero-dots span{width:9px;height:9px;border-radius:50%;background:var(--white)}
.hero-dots span.active{background:var(--red)}
.feature{top:700px;width:469px}
.feature-photo{height:205px;border:1px solid #ccc}
.feature h3{margin-top:15px;font-family:"Titillium Web",sans-serif;font-weight:600;font-size:18px;color:var(--red)}
.feature p{margin-top:4px;font-size:12.4px;line-height:24px}
.learn-more{display:block;text-align:right;margin-top:6px;padding-right:8px;font-style:italic;font-size:12.4px;color:var(--red)}
.section-title{font-family:"Titillium Web",sans-serif;font-weight:600;font-size:22px;color:var(--red)}
.news-card{top:1212px;width:318px}
.news-photo{height:191px;border:1px solid #ccc}
.news-card p{margin-top:10px;height:86px;font-size:12px;line-height:24px}
.btn-more{display:inline-block;margin-top:6px;width:100px;height:28px;line-height:28px;text-align:center;background:var(--red);color:var(--white);font-family:"Titillium Web",sans-serif;font-weight:600;font-size:12.5px;border-radius:2px}
.donation{left:99px;top:1596px;width:631px;height:120px;display:flex}
.donation-copy{width:446px;background:var(--grey-panel);border-left:5px solid var(--red);padding:26px 0 0 15px;color:var(--white)}
.donation-copy h2{font-family:"Titillium Web",sans-serif;font-weight:600;font-size:23px;line-height:28px}
.donation-copy p{margin-top:7px;font-size:14.5px}
.donation-action{flex:1;background:var(--red);color:var(--white);font-family:"Titillium Web",sans-serif;font-weight:600;font-size:19px;display:flex;align-items:center;justify-content:center}
.gauge{left:780px;top:1586px}
.testimonial{top:1816px;width:470px;font-size:12.4px;line-height:24px}
.testimonial p{padding-left:20px}
.testimonial cite{display:block;text-align:right;padding-right:30px;font-style:italic;font-size:12px;color:#333}
.quote-mark{position:absolute;font-family:Georgia,serif;font-size:38px;color:#777;line-height:1}
.footer-rule{left:0;top:1936px;width:1200px;height:7px;background:var(--red)}
.footer{left:0;top:1943px;width:1200px;height:237px;background:var(--footer)}
.footer-col{position:absolute;top:16px}
.footer-col h4{font-family:"Titillium Web",sans-serif;font-weight:400;font-size:17px;color:var(--white);margin-bottom:8px}
.footer-col li{list-style:none;font-size:12px;line-height:24px;color:var(--footer-text)}
.footer-base{left:0;top:2180px;width:1200px;height:64px;background:var(--footer-base)}
.copyright{position:absolute;left:103px;top:24px;font-size:12px;color:var(--footer-text)}
.social{position:absolute;left:980px;top:20px;display:flex;gap:8px}
.social span{width:24px;height:24px;background:#6d6d6d;border-radius:2px}
</style>
</head>
<body>
<div class="abs top-rule"></div>

<header class="abs brand">
  <div class="brand-mark"></div>
  <div class="brand-name">Hearth Lantern Promise</div>
</header>

<nav class="abs main-nav">
  <a style="left:142px">Home</a>
  <a style="left:225px">About</a>
  <a style="left:311px">About Gun Violence</a>
  <a style="left:475px">Get Involved</a>
  <a style="left:597px">Donate</a>
  <a style="left:689px">Events</a>
  <a style="left:779px">In Memoriam</a>
  <a style="left:907px">Blog</a>
  <a style="left:982px">Contact</a>
</nav>

<section class="abs hero">
  <div class="hero-photo" role="img" aria-label="Silhouette of a hanging bell against a sunset sky"></div>
  <div class="hero-quote">
    Sail past, quiet moon, to the evening sky,<br>
    The drifting cloud, the frosty light<br>
    The year is dying in the night; - Sir Edwin Marchbank
  </div>
  <svg class="hero-arrow" style="left:46px" viewBox="0 0 30 30"><circle cx="15" cy="15" r="15" fill="#fff"/><path d="M18 8 L11 15 L18 22" fill="none" stroke="#333" stroke-width="3"/></svg>
  <svg class="hero-arrow" style="left:1117px" viewBox="0 0 30 30"><circle cx="15" cy="15" r="15" fill="#fff"/><path d="M12 8 L19 15 L12 22" fill="none" stroke="#333" stroke-width="3"/></svg>
  <div class="hero-dots"><span class="active"></span><span></span><span></span></div>
</section>

<article class="abs feature" style="left:99px">
  <div class="feature-photo" role="img" aria-label="Protest sign reading that arms are for hugging" style="background:linear-gradient(135deg,#6b5e50,#c9bba3 45%,#8a7a6a)"></div>
  <h3>Lorem Ipsum</h3>
  <p>Lorem ipsum dolor sit amet, consectetuer adipiscing elit, sed diam nonummy nibh euismod tincidunt ut laoreet dolore magna aliquam erat volutpat. Ut wisi enim ad minim veniam, quis nostrud exerci tation ullamcorper suscipit lobortis nisl ut aliquip ex ea commodo consequat. Lorem ipsum dolor sit amet, consectetuer adipiscing elit, sed diam nonummy nibh euismod tincidunt ut laoreet dolore magna aliquam erat volutpat. Ut wisi enim ad minim veniam, quis nostrud exerci tation ullamcorper suscipit lobortis nisl ut aliquip ex ea commodo consequat.</p>
  <span class="learn-more">-Learn more....</span>
</article>
<article class="abs feature" style="left:631px">
  <div class="feature-photo" role="img" aria-label="Marchers holding a banner calling to end gun violence" style="background:linear-gradient(180deg,#7b6a6a,#d9d6d2 40%,#efefef 70%,#8f8f8f)"></div>
  <h3>Lorem Ipsum</h3>
  <p>Lorem ipsum dolor sit amet, consectetuer adipiscing elit, sed diam nonummy nibh euismod tincidunt ut laoreet dolore magna aliquam erat volutpat. Ut wisi enim ad minim veniam, quis nostrud exerci tation ullamcorper suscipit lobortis nisl ut aliquip ex ea commodo consequat. Lorem ipsum dolor sit amet, consectetuer adipiscing elit, sed diam nonummy nibh euismod tincidunt ut laoreet dolore magna aliquam erat volutpat. Ut wisi enim ad minim veniam, quis nostrud exerci tation ullamcorper suscipit lobortis nisl ut aliquip ex ea commodo consequat.</p>
  <span class="learn-more">-Learn more....</span>
</article>

<h2 class="abs section-title" style="left:99px;top:1163px">Latest From HLP</h2>

<article class="abs news-card" style="left:99px">
  <div class="news-photo" role="img" aria-label="Stadium billboard showing daily gun violence statistics" style="background:linear-gradient(180deg,#6f93c9,#a9c2e2 45%,#2a3140 60%,#d8d8d8)"></div>
  <p>Birchmore Kitchens in Larkvale will help you create the perfect kitchen. Whether you're after a modern kitchen or classic kitchen design we can design you a kitchen to suit your budget</p>
  <span class="btn-more">More info</span>
</article>
<article class="abs news-card" style="left:441px">
  <div class="news-photo" role="img" aria-label="Black and white photo of a child holding a handwritten sign asking for safety" style="background:linear-gradient(90deg,#2a2a2a,#6a6a6a 50%,#cfcfcf 75%,#4a4a4a)"></div>
  <p>Owner and operator of Birchmore Kitchens, Owen Pritchard has a building background and has been designing and manufacturing quality New Zealand made kitchens since 1982. If you dream of redesigning</p>
  <span class="btn-more">More info</span>
</article>
<article class="abs news-card" style="left:782px">
  <div class="news-photo" role="img" aria-label="Portrait of a campaign supporter outdoors" style="background:linear-gradient(135deg,#d7dbe0,#9a8a80 50%,#6b5d56)"></div>
  <p>Want to save time, stress and money on your new kitch­en? Choose Birchmore Kitchens to completely project manage your kitchen renovations. For one quote with no hidden costs and support from</p>
  <span class="btn-more">More info</span>
</article>

<section class="abs donation">
  <div class="donation-copy">
    <h2>Make a donation</h2>
    <p>All your funds goes to New Gun Laws policies Campaign</p>
  </div>
  <div class="donation-action">Donate</div>
</section>

<svg class="abs gauge" width="330" height="135" viewBox="0 0 330 135" role="img" aria-label="Donation level gauge">
  <g stroke="#333" stroke-width="0.8">
    <path d="M160 125 L50 125 A110 110 0 0 1 58.4 82.9 Z" fill="#fff35a"/>
    <path d="M160 125 L58.4 82.9 A110 110 0 0 1 82.2 47.2 Z" fill="#ffe640"/>
    <path d="M160 125 L82.2 47.2 A110 110 0 0 1 117.9 23.4 Z" fill="#ffd23a"/>
    <path d="M160 125 L117.9 23.4 A110 110 0 0 1 160 15 Z" fill="#ffb531"/>
    <path d="M160 125 L160 15 A110 110 0 0 1 202.1 23.4 Z" fill="#ff9a2c"/>
    <path d="M160 125 L202.1 23.4 A110 110 0 0 1 237.8 47.2 Z" fill="#ff6f2b"/>
    <path d="M160 125 L237.8 47.2 A110 110 0 0 1 261.6 82.9 Z" fill="#ff4a2d"/>
    <path d="M160 125 L261.6 82.9 A110 110 0 0 1 270 125 Z" fill="#f2232a"/>
  </g>
  <circle cx="160" cy="125" r="48" fill="#fff"/>
  <rect x="40" y="125" width="240" height="10" fill="#fff"/>
  <line x1="160" y1="125" x2="214" y2="80" stroke="#111" stroke-width="2"/>
  <g font-family="Open Sans, sans-serif" font-size="8" fill="#222">
    <text x="40" y="130">0</text>
    <text x="64" y="52">100</text>
    <text x="150" y="10">200</text>
    <text x="246" y="45">300</text>
    <text x="274" y="130">400</text>
    <text x="2" y="100">Low</text>
    <text x="70" y="22">Steady</text>
    <text x="180" y="8">Strong</text>
    <text x="270" y="70">Bold</text>
    <text x="284" y="108">Peak</text>
  </g>
</svg>

<h2 class="abs section-title" style="left:99px;top:1757px">Testimonials</h2>

<blockquote class="abs testimonial" style="left:99px">
  <span class="quote-mark" style="left:0;top:-6px">&ldquo;</span>
  <p>Lorem ipsum dolor sit amet, consectetuer adipiscing elit. Aenean commodo ligula eget dolor. Aenean massa. Cum sociis natoque penatibus et</p>
  <cite>-Marcus Eldon, CEO</cite>
  <span class="quote-mark" style="right:8px;top:52px">&rdquo;</span>
</blockquote>
<blockquote class="abs testimonial" style="left:614px">
  <span class="quote-mark" style="left:0;top:-6px">&ldquo;</span>
  <p>Lorem ipsum dolor sit amet, consectetuer adipiscing elit. Aenean commodo ligula eget dolor. Aenean massa. Cum sociis natoque penatibus et</p>
  <cite>-Marcus Eldon, CEO</cite>
  <span class="quote-mark" style="right:-16px;top:52px">&rdquo;</span>
</blockquote>

<div class="abs footer-rule"></div>
<footer class="abs footer">
  <div class="footer-col" style="left:100px">
    <h4>About Us</h4>
    <ul><li>NRT History</li><li>NRT Board</li><li>National Coverage</li><li>Quality Management System</li><li>Industry Partnerships</li></ul>
  </div>
  <div class="footer-col" style="left:302px;width:190px">
    <h4>Solutions &amp; Services</h4>
    <ul><li>Strategy and Architecture</li><li>Program and Project Manage­ment</li><li>Business Analysis</li><li>Application Development</li><li>Solution Testing &amp; Quality Management</li></ul>
  </div>
  <div class="footer-col" style="left:536px">
    <h4>Careers</h4>
    <ul><li>Excellence Together</li><li>The Recruitment Process</li><li>Graduates</li><li>Apply</li></ul>
  </div>
  <div class="footer-col" style="left:739px">
    <h4>Investor Centre</h4>
    <ul><li>Share Price</li><li>Financial Reports</li><li>Market Announcements</li><li>Corporate Governance</li></ul>
  </div>
  <div class="footer-col" style="left:942px">
    <h4>Other</h4>
    <ul><li>Contact</li><li>Privacy</li><li>Environment</li><li>Diversity</li></ul>
  </div>
</footer>
<div class="abs footer-base">
  <div class="copyright">© 2014 Company Name &nbsp;All right reserved &nbsp;Term of Use</div>
  <div class="social"><span></span><span></span><span></span><span></span></div>
</div>
</body>
</html>
```